Moden - Mexicali - Flower Shop

brisapetals is looking for a cool web design that has a airy, clean, mexicali feel to it.

See attached images and links for idea of what we mean with the above.

please no templates.

Target Market(s)

Local flower shop in San Diego, California

Industry/Entity Type

Shop

Requirements
Must have
• see. brisapetals.quartzcart.example - I did the site and logo...I love the logo - hate the site.

Going for this feel: http://www.velmorastudio.example/platebook/archives/tovarinos.php

I also attached another site I liked- I just feel like it may be to busy.

```html
<!DOCTYPE html>
<html lang="en">
<head>
<meta charset="utf-8">
<title>Brisa Petals – Flower Shop</title>
<link rel="stylesheet" href="https://fonts.googleapis.com/css2?family=Raleway:wght@300;400&family=Arimo:wght@400;600;700&family=Dancing+Script:wght@700&display=swap">
<style>
  :root {
    --page-bg: #ffffff;
    --ink: #5a5a5a;
    --ink-soft: #8d8d8d;
    --wine: #8a2d3b;
    --pink: #f06ba0;
    --pink-deep: #ec5f8f;
    --cart-plum: #a5606b;
    --rule: #c9c9c9;
    --topbar-line: #f3e07a;
    --nav-pink: rgba(240, 178, 186, 0.88);
    --nav-yellow: rgba(240, 226, 140, 0.9);
    --nav-blue: rgba(196, 228, 246, 0.9);
    --nav-green: rgba(190, 236, 172, 0.9);
    --menu-olive: #d2c57e;
    --menu-line: #e6dcaa;
    --foot-yellow: #fbf2c6;
    --foot-pink: #f3c8c8;
    --foot-green: #c8efbc;
  }
  * { box-sizing: border-box; margin: 0; padding: 0; }
  html, body { width: 943px; height: 1200px; overflow: hidden; }
  body {
    position: relative;
    background: var(--page-bg);
    font-family: "Arimo", Arial, sans-serif;
    color: var(--ink);
  }
  .abs { position: absolute; }

  /* hero */
  .hero-photo {
    position: absolute; left: 0; top: 0; width: 943px; height: 418px;
    background:
      radial-gradient(ellipse 260px 170px at 420px 150px, #f2a9c8 0%, rgba(242,169,200,0) 100%),
      radial-gradient(ellipse 200px 120px at 700px 130px, #f6b8d2 0%, rgba(246,184,210,0) 100%),
      radial-gradient(ellipse 220px 130px at 820px 60px, #e7f2b4 0%, rgba(231,242,180,0) 100%),
      linear-gradient(180deg, #eef3cf 0%, #f4d2df 40%, #b39a83 72%, #8f7a66 100%);
  }
  .topbar {
    position: absolute; left: 0; top: 0; width: 943px; height: 36px;
    background: rgba(255,255,255,0.82);
    border-bottom: 3px solid var(--topbar-line);
    font-size: 9.5px; color: var(--ink-soft);
  }
  .topbar span, .topbar .login { position: absolute; top: 12px; }
  .search-field { position: absolute; left: 146px; top: 10px; width: 82px; height: 17px; border: 1px solid #d27aa0; background: #fff; border-radius: 2px; }
  .login { left: 450px; top: 10px !important; width: 44px; height: 16px; border: 1px solid #7a7a7a; text-align: center; line-height: 14px; color: #555; }
  .cart-total {
    position: absolute; left: 723px; top: 5px; width: 42px; height: 42px; border-radius: 50%;
    background: var(--cart-plum); color: #fff; font-size: 10px; text-align: center; line-height: 42px;
  }
  .brand {
    position: absolute; left: 244px; top: 100px; width: 428px; height: 74px;
    background: rgba(255,255,255,0.85);
    display: flex; align-items: center; justify-content: center; gap: 16px;
    font-family: "Raleway", Arial, sans-serif; font-weight: 300; font-size: 34px; letter-spacing: 7px; color: #9fb7b8;
  }
  .brand-dot { width: 30px; height: 30px; border-radius: 50%; border: 2px solid #9fb7b8; }
  .collection-tag {
    position: absolute; left: 368px; top: 182px; width: 172px; height: 29px;
    background: rgba(255,255,255,0.88); text-align: center; line-height: 29px;
    font-family: "Dancing Script", cursive; font-size: 17px; color: #7a6d6d;
  }
  .btn {
    background: var(--pink); color: #fff; font-size: 9.5px; text-align: center;
    border-bottom: 2px solid #d4507f;
  }
  .view-now { position: absolute; left: 412px; top: 232px; width: 85px; height: 20px; line-height: 18px; }
  .slider-dots { position: absolute; left: 622px; top: 354px; display: flex; gap: 4px; }
  .slider-dots i { width: 11px; height: 11px; border-radius: 50%; border: 1px solid #fff; display: block; }
  .slider-dots i.on { background: #fff; }

  /* main nav */
  .main-nav { position: absolute; left: 70px; top: 382px; width: 812px; height: 36px; display: flex; font-size: 12px; }
  .main-nav a { display: block; text-align: center; line-height: 36px; color: #fff; text-decoration: none; }
  .nav-home { width: 200px; background: var(--nav-pink); color: #5a4a4a !important; }
  .nav-shop { width: 206px; background: var(--nav-yellow); }
  .nav-curated { width: 204px; background: var(--nav-blue); }
  .nav-about { width: 202px; background: var(--nav-green); }
  .shop-menu { position: absolute; left: 270px; top: 418px; width: 206px; background: var(--menu-olive); z-index: 5; font-size: 9px; color: #fff; }
  .shop-menu li { list-style: none; height: 23.5px; line-height: 23px; padding-left: 17px; border-bottom: 1px solid var(--menu-line); position: relative; }
  .shop-menu li:last-child { border-bottom: 0; }
  .shop-menu svg { position: absolute; right: 14px; top: 7px; }

  /* section headings */
  .section-rule { position: absolute; height: 1px; background: var(--rule); }
  .section-title {
    position: absolute; background: #fff; border: 1px solid var(--rule);
    font-family: "Dancing Script", cursive; font-size: 18px; color: var(--wine); text-align: center;
  }

  /* products */
  .product { position: absolute; top: 494px; width: 203px; }
  .product-photo { width: 203px; height: 202px; position: relative; }
  .product-name { margin-top: 16px; font-size: 11px; font-weight: 700; color: var(--wine); height: 14px; }
  .product-rule { margin-top: 5px; height: 1px; background: var(--rule); }
  .product-buy { margin-top: 6px; display: flex; align-items: center; height: 22px; font-size: 11px; }
  .price { color: var(--pink-deep); }
  .price-old { color: var(--ink-soft); text-decoration: line-through; margin-left: 8px; }
  .buy-now { margin-left: auto; width: 86px; height: 21px; line-height: 19px; }
  .zoom { position: absolute; left: 80px; top: 80px; }
  .carousel-arrow { position: absolute; top: 584px; }

  /* curated */
  .collection { position: absolute; top: 848px; text-align: center; }
  .collection-photo { height: 156px; }
  .collection-name { margin-top: 10px; font-size: 12px; color: #4a4a4a; }
  .collection-count { font-family: "Dancing Script", cursive; font-size: 11px; color: var(--pink-deep); }

  /* footer */
  .footer-panel { position: absolute; top: 1072px; height: 128px; padding: 14px 20px; font-size: 9.5px; line-height: 18px; color: #6a6a6a; }
  .footer-panel h3 { font-size: 9.5px; font-weight: 700; color: #5a4a4a; margin-bottom: 8px; letter-spacing: .3px; }
  .panel-meet { left: 72px; width: 258px; background: var(--foot-yellow); }
  .panel-reach { left: 330px; width: 276px; background: var(--foot-pink); }
  .panel-news { left: 606px; width: 248px; background: var(--foot-green); }
  .panel-meet h3 { display: flex; align-items: center; gap: 10px; }
  .newsletter-form { display: flex; gap: 6px; margin-top: 12px; }
  .email-field { width: 148px; height: 21px; background: #ececec; border: 1px solid #d8d8d8; padding-left: 12px; font-size: 9px; line-height: 19px; color: #999; }
  .sign-up { width: 61px; height: 21px; line-height: 19px; font-weight: 600; }
</style>
</head>
<body>

<div class="hero-photo" role="img" aria-label="Pink lisianthus bouquet in a woven basket with a pink ribbon on burlap, soft green background"></div>

<header class="topbar">
  <span style="left:108px">Search:</span>
  <div class="search-field"></div>
  <span style="left:354px">Are you a member?</span>
  <div class="login">LOG IN</div>
  <span style="left:512px">LOG OFF</span>
  <span style="left:620px">Check out the Cart</span>
  <svg class="abs" style="left:701px;top:9px" width="21" height="18" viewBox="0 0 21 18" fill="none" stroke="#8a8a8a" stroke-width="1.4">
    <path d="M1 2h3l2.5 10h10l2.5-7H5.5"/><circle cx="8" cy="15.5" r="1.4"/><circle cx="15" cy="15.5" r="1.4"/>
  </svg>
  <div class="cart-total">$ 0.00</div>
</header>

<div class="brand"><span>BRISA</span><i class="brand-dot"></i><span>PETALS</span></div>
<div class="collection-tag">spring collection</div>
<div class="btn view-now">VIEW NOW</div>
<div class="slider-dots"><i></i><i></i><i></i><i class="on"></i></div>

<nav class="main-nav">
  <a class="nav-home">HOME</a>
  <a class="nav-shop">SHOP</a>
  <a class="nav-curated">CURATED</a>
  <a class="nav-about">ABOUT US</a>
</nav>
<ul class="shop-menu">
  <li>Fresh this week<svg width="6" height="10" viewBox="0 0 6 10" fill="none" stroke="#fff"><path d="M1 1l4 4-4 4"/></svg></li>
  <li>Special collection<svg width="6" height="10" viewBox="0 0 6 10" fill="none" stroke="#fff"><path d="M1 1l4 4-4 4"/></svg></li>
  <li>Fresh this week<svg width="6" height="10" viewBox="0 0 6 10" fill="none" stroke="#fff"><path d="M1 1l4 4-4 4"/></svg></li>
  <li>Special collection</li>
</ul>

<div class="section-rule" style="left:77px;top:457px;width:795px"></div>
<div class="section-title" style="left:392px;top:440px;width:158px;height:34px;line-height:32px">Fresh this week</div>

<svg class="carousel-arrow" style="left:100px" width="16" height="30" viewBox="0 0 16 30" fill="none" stroke="#b5b5b5" stroke-width="1.4"><path d="M15 1L2 15l13 14"/></svg>
<svg class="carousel-arrow" style="left:812px" width="16" height="30" viewBox="0 0 16 30" fill="none" stroke="#b5b5b5" stroke-width="1.4"><path d="M1 1l13 14L1 29"/></svg>

<article class="product" style="left:127px">
  <div class="product-photo" role="img" aria-label="Bundle of deep red roses on weathered wood" style="background:linear-gradient(160deg,#8e2230,#6e1a26 55%,#b9aaa0)">
    <svg class="zoom" width="42" height="42" viewBox="0 0 42 42"><circle cx="21" cy="21" r="21" fill="#f06ba0"/><circle cx="19" cy="19" r="6" fill="none" stroke="#fff" stroke-width="2"/><path d="M23.5 23.5l5 5" stroke="#fff" stroke-width="2.4" stroke-linecap="round"/><path d="M16.5 19h5M19 16.5v5" stroke="#fff" stroke-width="1.6"/></svg>
  </div>
  <div class="product-name">CALIFORNIA LILLIES</div>
  <div class="product-rule"></div>
  <div class="product-buy"><span class="price">$ 50.00</span><span class="price-old">$ 75.00</span><div class="btn buy-now">BUY NOW</div></div>
</article>

<article class="product" style="left:362px">
  <div class="product-photo" role="img" aria-label="Yellow and orange lilies wrapped in paper on grey wood" style="background:radial-gradient(ellipse at 50% 40%,#f2c845,#e8843a 45%,#9a9a94 80%)"></div>
  <div class="product-name">RUBY ROSES</div>
  <div class="product-rule"></div>
  <div class="product-buy"><span class="price">$ 50.00</span><span class="price-old">$ 75.00</span><div class="btn buy-now">BUY NOW</div></div>
</article>

<article class="product" style="left:599px">
  <div class="product-photo" role="img" aria-label="Pink gerbera daisies in a kraft paper cone on grey wood" style="background:radial-gradient(ellipse at 50% 35%,#ec5c8e,#b89a78 55%,#8e8e8a 90%)"></div>
  <div class="product-name">RUBY ROSES</div>
  <div class="product-rule"></div>
  <div class="product-buy"><span class="price">$ 50.00</span><span class="price-old">$ 75.00</span><div class="btn buy-now">BUY NOW</div></div>
</article>

<div class="section-rule" style="left:72px;top:812px;width:810px"></div>
<div class="section-title" style="left:97px;top:797px;width:171px;height:31px;line-height:29px">Curated Collections</div>

<div class="collection" style="left:97px;width:139px">
  <div class="collection-photo" role="img" aria-label="Basket of purple and white daisies" style="background:radial-gradient(ellipse at 50% 40%,#8e3a8a,#e8e0e6 75%)"></div>
  <div class="collection-name">Any Occasion</div><div class="collection-count">1 product</div>
</div>
<div class="collection" style="left:239px;width:169px">
  <div class="collection-photo" role="img" aria-label="Pink tulips close up" style="background:linear-gradient(150deg,#a64a8a,#e48ab4 55%,#f3d0de)"></div>
  <div class="collection-name">Birthday</div><div class="collection-count">4 product</div>
</div>
<div class="collection" style="left:410px;width:143px">
  <div class="collection-photo" role="img" aria-label="Wicker basket of white daisies on a blue checked cloth" style="background:linear-gradient(180deg,#f4ecd8,#e8e6da 55%,#9bb4d0)"></div>
  <div class="collection-name">Dude</div><div class="collection-count">6 product</div>
</div>
<div class="collection" style="left:556px;width:140px">
  <div class="collection-photo" role="img" aria-label="Pink roses and white calla lilies in a glass vase" style="background:radial-gradient(ellipse at 50% 35%,#e98aa6,#eef0ee 70%)"></div>
  <div class="collection-name">Love</div><div class="collection-count">10 product</div>
</div>
<div class="collection" style="left:698px;width:155px">
  <div class="collection-photo" role="img" aria-label="Cream roses and yellow blooms in a wedding bouquet" style="background:radial-gradient(ellipse at 50% 35%,#f3e7c8,#f2f2ee 70%)"></div>
  <div class="collection-name">Wedding</div><div class="collection-count">5 product</div>
</div>

<footer>
  <section class="footer-panel panel-meet">
    <h3><svg width="22" height="22" viewBox="0 0 22 22"><circle cx="11" cy="11" r="10" fill="none" stroke="#6a5a4a" stroke-width="1.4"/><circle cx="11" cy="6.5" r="1.3" fill="#6a5a4a"/><path d="M11 9.5v7" stroke="#6a5a4a" stroke-width="2"/></svg>MEET BRISA</h3>
    <p>Rooted in Palmera Heights - We bring you hand-picked, seasonal, breezy, and same day delivery flower bundles.</p>
  </section>
  <section class="footer-panel panel-reach">
    <h3>REACH BRISA</h3>
    <p>2280 Marigold Avenue<br>San Diego, CA 92104</p>
    <p style="margin-top:4px"><b>Email:</b> info@brisapetals.com</p>
    <p style="margin-top:4px"><b>Phone:</b> 619-555-0147</p>
  </section>
  <section class="footer-panel panel-news">
    <h3>NEWSLETTER</h3>
    <p>We promise to only send you<br>good things like discounts!</p>
    <div class="newsletter-form"><div class="email-field">Your e-mail</div><div class="btn sign-up">SIGN UP</div></div>
  </section>
</footer>

</body>
</html>
```